Visitenkarten-Design für Psycho-Kinesiologie Praxis
Zielgruppe
praxis für Psycho-Kinesiologie - Systematische Familienaufstellungen. Einzelsitzungen Gruppentherapie
Ich suche ein Design was auf der einen Seite auffällt, aus dem Rahmen fällt und trotzdem seriös wirkt und Vertrauen schafft.
Die Anhänge sind nur meine Entwürfe also keine fixen Vorgaben
Aufgabenstellung
Eine Seite soll auffallen und Kreativ gestaltet sein
Es gibt ein Template aber die Farben sind noch nicht definiert.
https://www.vorlagenhafen.com/de/demo/48352.html
Es gibt ein Logo (Systemanalytiker) da sind die Farben auch nicht fix Definiert. Gerne sehe ich verschiedene Farbkombinationen
Foto: besseres folgt in kürze
Lumen Harbor Circle: Kann auf einer Seite drauf sein, wenn genug Platz,

```html
<!DOCTYPE html>
<html lang="de">
<head>
<meta charset="utf-8">
<title>Seelenweg – Visitenkarten</title>
<link href="https://fonts.googleapis.com/css2?family=Jost:wght@300;400;600&display=swap" rel="stylesheet">
<style>
  :root{
    --red:#d7182a;
    --graphite:#4a4a4a;
    --ink:#333333;
    --muted:#6f6f6f;
    --paper:#ffffff;
    --page:#ffffff;
  }
  *{margin:0;padding:0;box-sizing:border-box}
  html,body{width:854px;height:1200px;overflow:hidden;background:var(--page)}
  body{position:relative;font-family:"Jost",sans-serif;color:var(--ink)}

  .card{position:absolute;width:312px;height:202px;background:var(--paper);
        box-shadow:2px 3px 6px rgba(0,0,0,.22);overflow:hidden}
  .card.red{--accent:var(--red)}
  .card.grey{--accent:var(--graphite)}
  .col-front{left:101px}
  .col-back{left:445px}
  .row-1{top:107px}.row-2{top:371px}.row-3{top:635px}.row-4{top:899px}

  .side-bar{position:absolute;left:0;top:0;width:12px;height:100%;background:var(--accent)}
  .bottom-band{position:absolute;left:0;bottom:0;width:100%;height:15px;background:var(--accent);
        color:#fff;font-size:9.4px;line-height:15px;padding-left:7px;white-space:nowrap;letter-spacing:.1px}
  .claim{position:absolute;left:22px;bottom:3px;font-size:9.4px;white-space:nowrap;letter-spacing:.1px}

  /* Wortmarke */
  .brand{position:absolute;display:flex;align-items:center;gap:6px;font-weight:300;color:var(--ink);white-space:nowrap}
  .brand .dot{border-radius:50%;background:var(--red);flex:none}
  .brand-lg{left:52px;top:78px;font-size:36px}
  .brand-lg .dot{width:14px;height:14px}
  .brand-sm{left:158px;top:40px;font-size:21px}
  .band-back .brand-sm{left:160px}
  .brand-sm .dot{width:8px;height:8px}
  .tagline{position:absolute;font-weight:300;color:var(--muted);white-space:nowrap}
  .tagline-lg{right:53px;top:124px;font-size:9px}
  .tagline-sm{right:10px;top:70px;font-size:5px}
  .front-name{position:absolute;right:53px;top:140px;font-size:17px;font-weight:300;color:var(--muted)}

  /* Rückseite */
  .services{position:absolute;top:24px;list-style:none;font-size:8px;line-height:11.1px}
  .bar-back .services{left:22px}
  .band-back .services{left:7px;line-height:10.6px;font-size:7.6px}
  .services li::before{content:"|";color:var(--accent);margin-right:2px}
  .services li.cont::before{content:"";margin-right:5px}
  .band-back .services li::before{color:var(--red)}

  .person{position:absolute;font-size:8.2px;line-height:11px}
  .person strong{display:block;font-size:10.5px;font-weight:600}
  .bar-back .person{left:26px;top:116px}
  .band-back .person{left:165px;top:116px}

  .contact{position:absolute;list-style:none;font-size:8.2px;line-height:9.6px}
  .bar-back .contact{left:163px;top:119px}
  .band-back .contact{left:9px;top:109px;font-size:7.8px;line-height:9.2px}
  .contact li{display:flex;align-items:flex-start;gap:4px;margin-bottom:5.6px}
  .band-back .contact li{margin-bottom:4.8px}
  .contact li.line{margin-bottom:5.6px}
  .contact svg{width:7px;height:7px;flex:none;margin-top:1.5px;fill:var(--ink)}
  .band-back .contact svg{fill:var(--red)}
</style>
</head>
<body>
<svg width="0" height="0" style="position:absolute">
  <symbol id="ico-phone" viewBox="0 0 10 10"><path d="M2 0.5l2 2-1 1.2c.6 1.4 1.7 2.5 3.1 3.1l1.2-1 2 2-1.3 1.5C4.6 9.3 .7 5.4.5 1.8z"/></symbol>
  <symbol id="ico-mail" viewBox="0 0 10 10"><path d="M0 2h10v6H0z M.6 2.5L5 5.8 9.4 2.5" stroke="#fff" stroke-width=".8"/></symbol>
  <symbol id="ico-web" viewBox="0 0 10 10"><path d="M5 .5a4.5 4.5 0 1 0 0 9 4.5 4.5 0 1 0 0-9zm0 1a3.5 3.5 0 1 1 0 7 3.5 3.5 0 1 1 0-7z"/><path d="M1 5h8M5 1v8M2 3h6M2 7h6" stroke-width=".7" stroke="currentColor" fill="none"/></symbol>
</svg>

<!-- Reihe 1: Rot, Seitenbalken -->
<section class="card red col-front row-1">
  <div class="side-bar"></div>
  <div class="brand brand-lg"><span>Seelenweg</span><span class="dot"></span></div>
  <span class="tagline tagline-lg">Systemanalytiker</span>
  <p class="claim">Gesundheit - Glück - Liebe - Frieden - Version Klar - Version Kreativ</p>
</section>
<section class="card red col-back row-1 bar-back">
  <div class="side-bar"></div>
  <ul class="services"><li>Psycho-Kinesiologie</li><li class="cont">(nach Dr. Weißenberg)</li><li>Neurobiologie</li><li>Mentalfeldtherapie</li><li>Geistiges Familienstellen</li></ul>
  <div class="brand brand-sm"><span>Seelenweg</span><span class="dot"></span></div>
  <span class="tagline tagline-sm">Systemanalytiker</span>
  <p class="person"><strong>Udo Brandauer</strong>Systemanalytiker</p>
  <ul class="contact">
    <li><svg><use href="#ico-phone"/></svg><span>Schweiz<br>0041 791 555 042</span></li>
    <li><svg><use href="#ico-phone"/></svg><span>Deutschland<br>0049 170 555 48 12</span></li>
    <li><svg><use href="#ico-mail"/></svg><span>info@innenklar-praxis.ch</span></li>
    <li><svg style="color:var(--ink)"><use href="#ico-web"/></svg><span>www.innenklar-praxis.ch</span></li>
  </ul>
</section>

<!-- Reihe 2: Grau, Seitenbalken, mit Name -->
<section class="card grey col-front row-2">
  <div class="side-bar"></div>
  <div class="brand brand-lg"><span>Seelenweg</span><span class="dot"></span></div>
  <span class="tagline tagline-lg">Systemanalytiker</span>
  <p class="front-name">Udo Brandauer</p>
  <p class="claim">Gesundheit - Glück - Liebe - Frieden - Version Klar - Version Kreativ</p>
</section>
<section class="card grey col-back row-2 bar-back">
  <div class="side-bar"></div>
  <ul class="services"><li>Psycho-Kinesiologie</li><li class="cont">(nach Dr. Weißenberg)</li><li>Neurobiologie</li><li>Mentalfeldtherapie</li><li>Geistiges Familienstellen</li></ul>
  <div class="brand brand-sm"><span>Seelenweg</span><span class="dot"></span></div>
  <span class="tagline tagline-sm">Systemanalytiker</span>
  <p class="person"><strong>Udo Brandauer</strong>Systemanalytiker</p>
  <ul class="contact">
    <li><svg><use href="#ico-phone"/></svg><span>Schweiz<br>0041 791 555 042</span></li>
    <li><svg><use href="#ico-phone"/></svg><span>Deutschland<br>0049 170 555 48 12</span></li>
    <li><svg><use href="#ico-mail"/></svg><span>info@innenklar-praxis.ch</span></li>
    <li><svg style="color:var(--ink)"><use href="#ico-web"/></svg><span>www.innenklar-praxis.ch</span></li>
  </ul>
</section>

<!-- Reihe 3: Rot, Fußband -->
<section class="card red col-front row-3">
  <div class="brand brand-lg"><span>Seelenweg</span><span class="dot"></span></div>
  <span class="tagline tagline-lg">Systemanalytiker</span>
  <p class="bottom-band">Gesundheit - Glück - Liebe - Frieden - Version Klar - Version Kreativ</p>
</section>
<section class="card red col-back row-3 band-back">
  <ul class="services"><li>Psycho-Kinesiologie</li><li class="cont">(nach Dr. Weißenberg)</li><li>Neurobiologie</li><li>Mentalfeldtherapie</li><li>Geistiges Familienstellen</li></ul>
  <div class="brand brand-sm"><span>Seelenweg</span><span class="dot"></span></div>
  <span class="tagline tagline-sm">Systemanalytiker</span>
  <p class="person"><strong>Udo Brandauer</strong>Systemanalytiker</p>
  <ul class="contact">
    <li><svg><use href="#ico-phone"/></svg><span>Schweiz<br>0041 791 555 042</span></li>
    <li><svg><use href="#ico-phone"/></svg><span>Deutschland<br>0049 170 555 48 12</span></li>
    <li><svg><use href="#ico-mail"/></svg><span>info@innenklar-praxis.ch</span></li>
    <li><svg style="color:var(--red)"><use href="#ico-web"/></svg><span>www.innenklar-praxis.ch</span></li>
  </ul>
  <p class="bottom-band">Gesundheit - Glück - Liebe - Frieden - Version Klar - Version Kreativ</p>
</section>

<!-- Reihe 4: Grau, Fußband, mit Name -->
<section class="card grey col-front row-4">
  <div class="brand brand-lg"><span>Seelenweg</span><span class="dot"></span></div>
  <span class="tagline tagline-lg">Systemanalytiker</span>
  <p class="front-name">Udo Brandauer</p>
  <p class="bottom-band">Gesundheit - Glück - Liebe - Frieden - Version Klar - Version Kreativ</p>
</section>
<section class="card grey col-back row-4 band-back">
  <ul class="services"><li>Psycho-Kinesiologie</li><li class="cont">(nach Dr. Weißenberg)</li><li>Neurobiologie</li><li>Mentalfeldtherapie</li><li>Geistiges Familienstellen</li></ul>
  <div class="brand brand-sm"><span>Seelenweg</span><span class="dot"></span></div>
  <span class="tagline tagline-sm">Systemanalytiker</span>
  <p class="person"><strong>Udo Brandauer</strong>Systemanalytiker</p>
  <ul class="contact">
    <li><svg><use href="#ico-phone"/></svg><span>Schweiz<br>0041 791 555 042</span></li>
    <li><svg><use href="#ico-phone"/></svg><span>Deutschland<br>0049 170 555 48 12</span></li>
    <li><svg><use href="#ico-mail"/></svg><span>info@innenklar-praxis.ch</span></li>
    <li><svg style="color:var(--red)"><use href="#ico-web"/></svg><span>www.innenklar-praxis.ch</span></li>
  </ul>
  <p class="bottom-band">Gesundheit - Glück - Liebe - Frieden - Version Klar - Version Kreativ</p>
</section>
</body>
</html>
```